Menu Design for Chocolate and Cheese Shop

We are chocolate (and cheese) makers - www.velmarita.com.au and would like to redesign our café menu (attached is the pdf of the old one). I would like to end up with a file using Adobe suite of products so we can readily update menus as we change them. Clean, classy and inviting. We would also like to incorporate our cheese with our sister business into the menu offering (www.dunhollowmead.com.au and www.facebook.com/dunhollowmead). Just allow space for us to flesh out content for the cheese menu items - we will definitely include our Tall Platter in this if you see our facebook posts) - 4pp - A4 landscape folded into A5. We would also like the exact same menu but with our Dunhollow Mead Branding instead of velmarita (we have two different sites -attached are our dunhollow mead logos as well for incorporating into the second document)

```html
<!DOCTYPE html>
<html lang="en">
<head>
<meta charset="utf-8">
<title>Velmarita Café Menu</title>
<link rel="stylesheet" href="https://fonts.googleapis.com/css2?family=Kaushan+Script&family=Noto+Sans:wght@400;600&display=swap">
<style>
  :root{
    --page:#ecebe8;
    --menu-deep:#5e0c04;
    --menu-mid:#9c2208;
    --menu-warm:#c8410f;
    --ornament:#e07a16;
    --panel-a:rgba(150,30,6,.78);
    --panel-b:rgba(90,10,4,.82);
    --gold:#ffc21a;
    --text:#ffffff;
  }
  *{margin:0;padding:0;box-sizing:border-box}
  html,body{width:1200px;height:1200px;overflow:hidden;background:var(--page)}
  .canvas{position:relative;width:1200px;height:1200px}
  .menu{
    position:absolute;left:18px;top:189px;width:1164px;height:822px;
    background:linear-gradient(135deg,var(--menu-deep),var(--menu-mid) 45%,var(--menu-warm) 70%,var(--menu-deep));
    box-shadow:6px 8px 14px rgba(0,0,0,.35);
    overflow:hidden;
  }
  .ornament-band{position:absolute;left:0;width:100%;height:26px;
    background:linear-gradient(90deg,var(--menu-deep),var(--ornament),var(--menu-deep),var(--ornament),var(--menu-deep))}
  .ornament-band.top{top:0}
  .ornament-band.bottom{bottom:0;height:28px}
  .ornament-side{position:absolute;top:26px;bottom:28px;width:24px;
    background:linear-gradient(180deg,var(--menu-deep),#8a2a08,var(--menu-deep))}
  .ornament-side.left{left:0}
  .ornament-side.right{right:0}
  .panel{position:absolute;top:24px;height:772px;
    background:linear-gradient(160deg,var(--panel-a),var(--panel-b))}
  .panel.treats{left:24px;width:554px}
  .panel.drinks{left:581px;width:558px}
  .section-title,.kids-title{
    position:absolute;font-family:"Kaushan Script",cursive;color:var(--gold);
    font-size:30px;line-height:34px;text-shadow:1px 1px 0 #5a0a02;
  }
  .item{position:absolute;font-family:"Noto Sans",sans-serif;color:var(--text)}
  .col-left{left:38px;width:532px}
  .col-right{left:598px;width:540px}
  .item h3{font-weight:400;color:var(--gold);font-size:18px;line-height:25px;letter-spacing:.3px}
  .item p{font-size:14.5px;line-height:25px;letter-spacing:.4px;font-weight:600;text-align:justify}
  .kids-box{position:absolute;left:40px;top:682px;width:524px;height:97px;
    border:2px solid var(--gold);border-radius:3px}
  .kids-title{left:0;right:0;top:-24px;text-align:center}
  .kids-title span{background:linear-gradient(90deg,#6c1005,#741306);padding:0 28px}
  .kids-list{position:absolute;list-style:none;font-family:"Noto Sans",sans-serif;
    color:var(--text);font-size:14.5px;line-height:25.5px;font-weight:600;letter-spacing:.3px;top:12px}
  .kids-list.first{left:4px}
  .kids-list.second{left:312px}
  .kids-list li::before{content:"";display:inline-block;width:8px;height:8px;border-radius:50%;
    background:var(--gold);margin-right:5px;vertical-align:1px}
</style>
</head>
<body>
<div class="canvas">
  <div class="menu">
    <div class="ornament-band top" role="img" aria-label="Gold scrollwork border"></div>
    <div class="ornament-band bottom" role="img" aria-label="Gold scrollwork border"></div>
    <div class="ornament-side left" role="img" aria-label="Gold scroll ornaments"></div>
    <div class="ornament-side right" role="img" aria-label="Gold scroll ornaments"></div>

    <div class="panel treats" role="img" aria-label="Warm-toned photo of cupcakes, mousse jars and cookies"></div>
    <div class="panel drinks" role="img" aria-label="Warm-toned photo of a hot chocolate cup, truffles and coffee beans"></div>

    <!-- Sweet treats -->
    <h2 class="section-title" style="left:58px;top:26px">Sweet Treats</h2>
    <div class="item col-left" style="top:66px"><h3>Chocolate taste plate - $14.30</h3><p>Chocolate macaron, chocolateice cream, chocolate mousse, and our signature chocolate</p></div>
    <div class="item col-left" style="top:150px"><h3>Caramel taste plate - $14.30</h3><p>Caramel slice, hokey pokey ice cream, caramel truffle, and alfajores (Spanish shortbread) filled with dulce de leche</p></div>
    <div class="item col-left" style="top:234px"><h3>Raspberry brownie - $12.50</h3><p>Brownie topped with raspberries, served warm with a scoop of vanilla bean ice cream</p></div>
    <div class="item col-left" style="top:318px;left:40px"><h3>Ice cream sensation - $12.00</h3><p>A trio of chocolate ice cream or our weekly special ice cream served with chocolate sauce and sprinkled with dark crispy pearls (ask our team what flavour is available)</p></div>
    <div class="item col-left" style="top:432px"><h3>Chocolate mousse - $12.00</h3><p>Rich and creamy chocolate mousse served with white crispy pearls</p></div>
    <div class="item col-left" style="top:494px"><h3>Handmade chocolates – from $1.90</h3><p>Choose from our extensive range of fresh chocolates and truffles</p></div>
    <div class="item col-left" style="top:557px"><h3>Dessert jars - $15.50</h3><p style="margin-top:4px">Ask our team to find out what is on offer this week</p></div>
    <div class="item col-left" style="top:620px;left:40px"><h3>Handmade cookies - $3.00</h3></div>

    <div class="kids-box">
      <h2 class="kids-title"><span>For the Children</span></h2>
      <ul class="kids-list first">
        <li>Mini hot chocolate - $3.00</li>
        <li>Mini chino - $1.00</li>
        <li>Mini chino with teddy pop - $2.50</li>
      </ul>
      <ul class="kids-list second">
        <li>Mini ice chocolate - $5.00</li>
        <li>Mini icecream - $3.50</li>
        <li>Mini mousse - $3.50</li>
      </ul>
    </div>

    <!-- Drinks -->
    <h2 class="section-title" style="left:600px;top:26px">Drinks</h2>
    <div class="item col-right" style="top:66px"><h3>Hot chocolate – reg $5.50 – lrg $6.00</h3><p>Traditional – made with 65% maracaibo single origin chocolate white – made with white chocolate<br>Half and half – half traditional and half white hot chocolate</p></div>
    <div class="item col-right" style="top:170px"><h3>Mocha – reg $6.00 – lrg $6.50</h3><p style="line-height:19px">Can be made with traditional or white chocolate</p></div>
    <div class="item col-right" style="top:222px"><h3>Special hot chocolate - $6.50 – lrg $7.00</h3><p>A creamy ganache made with crème fraiche infused with a different flavour each week (ask our team what flavour is available)</p></div>
    <div class="item col-right" style="top:302px"><h3>Coffee – reg $4.00 – lrg $4.50</h3><p>Latte, cappuccino, flat white, long black, short black, short macchiato, long macchiato, piccolo latte</p></div>
    <div class="item col-right" style="top:381px"><h3>Chai – reg $4.00 – lrg $4.50</h3><h3>Tea – a pot of Leafwell organic tea - $5.00</h3><p>English breakfast, earl grey, french earl grey, wellbeing, coconut, berry green, white tea and rose, chai, dark tea &amp; chocolate, lemongrass and ginger</p></div>
    <div class="item col-right" style="top:512px"><h3>Affogato - 6.00</h3><p style="margin-top:1px">Vanilla bean icream served with a shot of coffee or molten chocolate</p></div>
    <div class="item col-right" style="top:569px"><h3>Iced coffee - $5.50</h3><h3>Iced chocolate - $7.00 - white or 65% maracaibo single origin chocolate</h3><p>Our special blend of Fernvale cream, milk, and chocolate</p></div>
    <div class="item col-right" style="top:674px"><h3>Iced mocha – white or traditional - $7.50</h3><h3 style="line-height:27px">Milkshakes - $6.00</h3><p style="line-height:20px">Chocolate, (our own decadent fudge, vanilla or caramel)</p></div>
    <div class="item col-right" style="top:757px"><h3>Clearbrook – still or sparkling water $3.00</h3></div>
  </div>
</div>
</body>
</html>
```